Webbanner-Design für Online Pfandhaus
Zielgruppe
Online Pfandhaus
Aufgabenstellung
Der Banner für unsere Webseite soll neu gestaltet werden. (Siehe Bilddatei)
Ziel ist es einen schönen, konvertierenden Banner zu gestalten. Der Banner soll sich an die Seite anpassen.
Der Banner wird dann auch für Social Media benötigt.

```html
<!DOCTYPE html>
<html lang="de">
<head>
<meta charset="utf-8">
<title>leihKontor.de – Online-Pfandhaus</title>
<link href="https://fonts.googleapis.com/css2?family=Open+Sans:wght@400;700&family=Oswald:wght@500&display=swap" rel="stylesheet">
<style>
  :root {
    --navy: #2b3f95;
    --band-dark: #283f92;
    --band-light: #2d48a1;
    --gold: #f9b60e;
    --white: #ffffff;
    --field: #f7f7fb;
    --ink: #222a3a;
    --art-a: #6a63e0;
    --art-b: #3d3bb0;
  }
  * { margin: 0; padding: 0; box-sizing: border-box; }
  html, body { width: 1200px; height: 600px; overflow: hidden; background: var(--white); }
  body { position: relative; font-family: "Open Sans", sans-serif; }

  .site-header { position: absolute; top: 0; left: 0; width: 1200px; height: 62px; background: var(--white); }
  .brand { position: absolute; left: 154px; top: 16px; display: flex; align-items: center; gap: 8px;
    font-family: "Open Sans", sans-serif; font-weight: 700; font-size: 18px; color: var(--navy); }
  .brand-dot { width: 28px; height: 28px; border-radius: 50%; background: var(--navy); }
  .main-nav { position: absolute; left: 439px; top: 17px; display: flex; gap: 29px;
    font-family: "Oswald", sans-serif; font-weight: 500; font-size: 17px; color: var(--navy); }
  .main-nav span { white-space: nowrap; }
  .caret { display: inline-block; margin-left: 6px; vertical-align: 2px; }

  .hero-band { position: absolute; top: 62px; left: 0; width: 1200px; height: 480px; }

  .hero-copy { position: absolute; left: 120px; width: 462px; text-align: center; color: var(--white); }
  .hero-title { position: absolute; top: 156px; left: 0; width: 100%; font-weight: 700; font-size: 38px;
    color: var(--gold); line-height: 1.2; }
  .hero-sub { position: absolute; top: 204px; left: 0; width: 100%; font-size: 18.5px; line-height: 25px; }
  .hero-label { position: absolute; top: 309px; left: 0; width: 100%; font-size: 12.5px; }
  .request-form { position: absolute; top: 340px; left: 85px; display: flex; height: 53px; }
  .item-select { width: 169px; background: var(--field); border-radius: 3px 0 0 3px; display: flex;
    align-items: center; justify-content: space-between; padding: 0 15px 0 22px; font-size: 14.5px; color: var(--ink); }
  .request-btn { width: 103px; background: var(--gold); border-radius: 0 3px 3px 0; display: flex;
    align-items: center; justify-content: center; font-weight: 700; font-size: 14.5px; color: var(--ink); }
  .hero-alt { position: absolute; top: 408px; left: 0; width: 100%; font-size: 12.5px; }
  .hero-alt u { text-underline-offset: 2px; }

  .hero-illustration { position: absolute; left: 592px; top: 94px; width: 406px; height: 382px;
    border-radius: 24px; background: radial-gradient(ellipse at 55% 50%, var(--art-a), var(--art-b) 75%, rgba(61,59,176,0) 100%); opacity: .85; }
</style>
</head>
<body>
  <header class="site-header">
    <div class="brand"><span class="brand-dot"></span>leihKontor.de</div>
    <nav class="main-nav">
      <span>Start</span><span>Anfrage</span><span>Ablauf</span>
      <span>Standorte<svg class="caret" width="9" height="6" viewBox="0 0 9 6"><path d="M1 1l3.5 3.5L8 1" fill="none" stroke="#2b3f95" stroke-width="1.5"/></svg></span>
      <span>Wissenswertes</span><span>FAQ</span><span>Kontakt</span><span>Über uns</span>
    </nav>
  </header>

  <svg class="hero-band" viewBox="0 0 1200 480" aria-hidden="true">
    <path d="M0 0H1200V407Q600 538 0 407Z" fill="var(--band-dark)"/>
    <path d="M0 356Q120 340 250 320Q420 296 560 322Q760 362 900 338Q1060 312 1200 330V407Q600 538 0 407Z" fill="var(--band-light)"/>
  </svg>

  <div class="hero-illustration" role="img" aria-label="Illustration: Smartphone als Ladengeschäft mit Markise, links ein Mann mit Diamant, rechts ein Mann mit großer Goldmünze, umgeben von Blättern und Schmuck-Icons"></div>

  <section class="hero-copy">
    <h1 class="hero-title">Ihr Online-Pfandhaus</h1>
    <p class="hero-sub">Bei uns erhalten Sie in kürzester Zeit Geld<br>für Ihre Wertgegenstände.</p>
    <p class="hero-label">Welchen Wertgegenstand möchten Sie beleihen?</p>
    <div class="request-form">
      <div class="item-select">Schmuck
        <svg width="13" height="8" viewBox="0 0 13 8"><path d="M1 1l5.5 5.5L12 1" fill="none" stroke="#222a3a" stroke-width="1.6"/></svg>
      </div>
      <div class="request-btn">Anfrage</div>
    </div>
    <p class="hero-alt">Alternativ können Sie uns auch direkt unter <u>ChatLine</u> kontaktieren</p>
  </section>
</body>
</html>
```